I need the Scorecard I've developed for my staff to be produced into a visually engaging piece that will encourage the staff to utilize it on a daily basis. I'm thinking it could be 5x7 in size so that it isn't too cumbersome, but I'm open to different layouts.
I have multiple other departments that will need Scorecards created for them as well, but each one will contain task specific questions for each department.

```html
<!DOCTYPE html>
<html lang="en">
<head>
<meta charset="utf-8">
<title>Receptionist Daily Excellence Scorecard</title>
<link href="https://fonts.googleapis.com/css2?family=Arimo:wght@400;700&family=Roboto+Condensed:wght@400;700&display=swap" rel="stylesheet">
<style>
:root{
  --frame:#d9302c;
  --title:#0e4e96;
  --bar:#5e5a5a;
  --ink:#222;
  --blue-h:#93cdf0; --blue-r:#cde6f7;
  --yellow-h:#e6cf7f; --yellow-r:#fbe99d;
  --violet-h:#c2b8d8; --violet-r:#e4dfef;
  --pink-h:#e396b0; --pink-r:#f9d5e3;
  --green-h:#a9cd5f; --green-r:#d3e8a2;
  --peach-h:#ecc09a; --peach-r:#f3dcc2;
  --grey-r:#dcdcdc;
  --mint-h:#84c19c; --mint-r:#c8e5d2;
  --orange-h:#eb9e4e; --orange-r:#f5d4b1;
  --plum-h:#9b3f7a; --plum-r:#e0c8dc;
  --sign:#1f5ea8;
  --red:#e03a3a; --cyan:#1aa0d8; --leaf:#2e9e3e;
}
*{box-sizing:border-box;margin:0;padding:0}
html,body{width:1200px;height:719px;overflow:hidden;background:#fff}
body{font-family:"Arimo",Arial,sans-serif;color:var(--ink)}
.canvas{position:relative;width:1200px;height:719px}
.page{position:absolute;top:77px;width:498px;height:564px;border:1.5px solid var(--frame)}
.page-front{left:81px}
.page-back{left:620px}
.abs{position:absolute}
.title{left:94px;top:84px;width:472px;height:30px}
.title text{font-family:"Roboto Condensed",sans-serif;font-size:28px;fill:var(--title)}
.field{position:absolute;border:1px solid #333;height:17px;font-size:10px;display:flex;align-items:center;padding-left:5px;gap:0;white-space:nowrap}
.field .date{margin-left:auto;margin-right:72px}
.legend-box{left:365px;top:115px;width:201px;height:36px;border:1px solid #333;text-align:center}
.legend-box .ask{font-size:9.5px;margin-top:6px;white-space:nowrap}
.legend-box .scale{font-family:"Roboto Condensed",sans-serif;font-size:7.5px;margin-top:5px;display:flex;justify-content:center;gap:5px;white-space:nowrap}
.scale .lo{color:var(--red)} .scale .mid{color:var(--cyan)} .scale .hi{color:var(--leaf)}

.section{position:absolute;width:471px}
.sec-head{height:17px;background:var(--bar);border-radius:7px 7px 0 0;display:flex;align-items:center;justify-content:center;gap:10px;color:#fff;font-weight:700;font-size:12.5px;letter-spacing:.2px;white-space:nowrap}
.sec-head svg{width:18px;height:20px;margin-top:-8px;flex:none}
.grid-row{display:grid;grid-template-columns:214px 59px 1fr;column-gap:1.5px;margin-top:1px;height:17.8px}
.grid-row>div{display:flex;align-items:center;padding-left:8px;font-size:10.3px;white-space:nowrap;overflow:hidden}
.col-head{height:18px}
.col-head>div{font-size:11px}
.col-head .rate{padding-left:0;justify-content:center}
.col-head .rate svg{width:57px;height:14px;display:block}
.col-head .rate text{font-family:"Roboto Condensed",sans-serif;font-size:10px;fill:var(--ink)}
.col-head .notes{justify-content:center;padding-left:0}
.blue .col-head>div{background:var(--blue-h)} .blue .task-row>div{background:var(--blue-r)}
.yellow .col-head>div{background:var(--yellow-h)} .yellow .task-row>div{background:var(--yellow-r)}
.violet .col-head>div{background:var(--violet-h)} .violet .task-row>div{background:var(--violet-r)}
.pink .col-head>div{background:var(--pink-h)} .pink .task-row>div{background:var(--pink-r)}
.green .col-head>div{background:var(--green-h)} .green .task-row>div{background:var(--green-r)}
.peach .col-head>div{background:var(--peach-h)} .peach .task-row>div{background:var(--peach-r)}

.band{height:18px;margin-top:1px;display:flex;align-items:center;font-size:10px;white-space:nowrap}
.status .band{background:var(--grey-r)}
.status .dot{width:14px;height:14px;border-radius:50%;background:#fff;margin-left:34px;flex:none}
.status .label{width:97px;padding-left:16px}
.reflect .sec-head{background:var(--mint-h)}
.reflect .band{background:var(--mint-r);padding:0 22px 0 23px}
.flags .sec-head{background:var(--orange-h)}
.flags .band{background:var(--orange-r);padding:0 22px 0 11px}
.fill-line{flex:1;border-bottom:1px dotted #555;height:9px;margin-left:2px}
.band svg{width:9px;height:9px;margin-right:4px;flex:none}
.manager{width:276px}
.manager .sec-head{background:var(--plum-h)}
.manager .band{background:var(--plum-r);padding-left:20px}
.manager .short{flex:none;width:62px}
.sign-box{left:917px;top:573px;width:187px;height:56px;border:1.5px solid var(--sign);border-radius:6px;font-size:11px;padding:5px 6px 0 7px}
.sign-line{display:flex;height:17px;align-items:center;white-space:nowrap}
.sign-line.date{padding-left:58px}
</style>
</head>
<body>
<div class="canvas">
  <div class="page page-front"></div>
  <div class="page page-back"></div>

  <svg class="abs title" viewBox="0 0 472 30"><text x="0" y="26" textLength="472" lengthAdjust="spacingAndGlyphs"><tspan font-weight="700">RECEPTIONIST</tspan> DAILY EXCELLENCE SCORECARD</text></svg>

  <div class="field" style="left:94px;top:115px;width:265px">Name :</div>
  <div class="field" style="left:94px;top:135px;width:265px">Location :<span class="date">Date :</span></div>
  <div class="abs legend-box">
    <div class="ask">Please Rate yourself for each task</div>
    <div class="scale"><span class="lo">1 = Needs Improvement</span><span class="mid">3 = Meets Expectations</span><span class="hi">5 = Excellent</span></div>
  </div>

  <div class="section blue" style="left:94px;top:160px">
    <div class="sec-head"><svg viewBox="0 0 18 20"><rect x="2" y="3" width="13" height="16" rx="1.5" fill="#1f7ac4"/><path d="M4 1v4M7 1v4M10 1v4M13 1v4" stroke="#1f7ac4" stroke-width="1.4"/><path d="M5 9h7M5 12h7M5 15h5" stroke="#fff" stroke-width="1.2"/></svg>1. Call Handling &amp; First Call Intake</div>
    <div class="grid-row col-head"><div>Task</div><div class="rate"><svg viewBox="0 0 57 14"><text x="1" y="11" textLength="55" lengthAdjust="spacingAndGlyphs">Self Rating (1-5)</text></svg></div><div class="notes">Notes / Issues</div></div>
    <div class="grid-row task-row"><div>Answered 90%+ calls within 3 rings</div><div></div><div></div></div>
    <div class="grid-row task-row"><div>Maintained empathy and professionalism</div><div></div><div></div></div>
    <div class="grid-row task-row"><div>Accurately completed all First Call fields</div><div></div><div></div></div>
    <div class="grid-row task-row"><div>Worked within Receptionist role</div><div></div><div></div></div>
  </div>

  <div class="section yellow" style="left:94px;top:278px">
    <div class="sec-head"><svg viewBox="0 0 18 20"><path d="M5 1c-2 1-3 3-2 7 1 5 4 9 8 11 2 1 3 0 4-1l-3-4-2 1c-2-2-3-4-3-7l2-1-2-5z" fill="#ef7d22"/></svg>2. Call Management During Busy Times</div>
    <div class="grid-row col-head"><div>Task</div><div class="rate"><svg viewBox="0 0 57 14"><text x="1" y="11" textLength="55" lengthAdjust="spacingAndGlyphs">Self Rating (1-5)</text></svg></div><div class="notes">Notes / Issues</div></div>
    <div class="grid-row task-row"><div>Prioritized urgent vs. non-urgent calls</div><div></div><div></div></div>
    <div class="grid-row task-row"><div>Hold times under 1 minute</div><div></div><div></div></div>
    <div class="grid-row task-row"><div>Logged all calls</div><div></div><div></div></div>
    <div class="grid-row task-row"><div>Requested help if overwhelmed</div><div></div><div></div></div>
  </div>

  <div class="section violet" style="left:94px;top:398px">
    <div class="sec-head"><svg viewBox="0 0 22 20" style="width:22px"><rect x="1" y="3" width="20" height="16" rx="1.5" fill="#8a7fc0"/><rect x="1" y="3" width="20" height="4" fill="#6f63a8"/><path d="M5 1v4M17 1v4" stroke="#6f63a8" stroke-width="1.5"/><g fill="#fff"><rect x="4" y="9" width="2.5" height="2"/><rect x="8" y="9" width="2.5" height="2"/><rect x="12" y="9" width="2.5" height="2"/><rect x="16" y="9" width="2.5" height="2"/><rect x="4" y="13" width="2.5" height="2"/><rect x="8" y="13" width="2.5" height="2"/><rect x="12" y="13" width="2.5" height="2"/><rect x="16" y="13" width="2.5" height="2"/></g></svg>3. Scheduling Accuracy</div>
    <div class="grid-row col-head"><div>Task</div><div class="rate"><svg viewBox="0 0 57 14"><text x="1" y="11" textLength="55" lengthAdjust="spacingAndGlyphs">Self Rating (1-5)</text></svg></div><div class="notes">Notes / Issues</div></div>
    <div class="grid-row task-row"><div>Updated scheduling board</div><div></div><div></div></div>
    <div class="grid-row task-row"><div>Cross-checked with Red Book</div><div></div><div></div></div>
    <div class="grid-row task-row"><div>Entered manifold info promptly</div><div></div><div></div></div>
  </div>

  <div class="section pink" style="left:94px;top:498px">
    <div class="sec-head"><svg viewBox="0 0 18 20"><path d="M6 1l-5 3 2 5 2-1v11h8V8l2 1 2-5-5-3c-1 2-5 2-6 0z" fill="#c0397a"/></svg>4. Clothing &amp; Flowers</div>
    <div class="grid-row col-head"><div>Task</div><div class="rate"><svg viewBox="0 0 57 14"><text x="1" y="11" textLength="55" lengthAdjust="spacingAndGlyphs">Self Rating (1-5)</text></svg></div><div class="notes">Notes / Issues</div></div>
    <div class="grid-row task-row"><div>Clothing sheet completed</div><div></div><div></div></div>
    <div class="grid-row task-row"><div>Family contact noted on sheet</div><div></div><div></div></div>
    <div class="grid-row task-row"><div>Floral deliveries logged</div><div></div><div></div></div>
    <div class="grid-row task-row"><div>Concerns communicated to Care Center</div><div></div><div></div></div>
    <div class="grid-row task-row"><div>Flower placement verified</div><div></div><div></div></div>
  </div>

  <div class="section green" style="left:633px;top:94px">
    <div class="sec-head"><svg viewBox="0 0 18 20"><rect x="2" y="1" width="14" height="18" rx="1.5" fill="none" stroke="#7cb342" stroke-width="1.5"/><path d="M9 5h5M9 8h5M5 12h9M5 15h9" stroke="#7cb342" stroke-width="1.2"/><circle cx="5.5" cy="6.5" r="2" fill="#7cb342"/></svg>5. Death Certificates</div>
    <div class="grid-row col-head"><div>Task</div><div class="rate"><svg viewBox="0 0 57 14"><text x="1" y="11" textLength="55" lengthAdjust="spacingAndGlyphs">Self Rating (1-5)</text></svg></div><div class="notes">Notes / Issues</div></div>
    <div class="grid-row task-row"><div>Verified recipient ID &amp; relationship</div><div></div><div></div></div>
    <div class="grid-row task-row"><div>Confirmed correct documents enclosed</div><div></div><div></div></div>
    <div class="grid-row task-row"><div>Recipient signed the DC logbook</div><div></div><div></div></div>
    <div class="grid-row task-row"><div>Suggested proofreading before leaving</div><div></div><div></div></div>
  </div>

  <div class="section peach" style="left:633px;top:221px">
    <div class="sec-head"><svg viewBox="0 0 20 20" style="width:20px"><path d="M10 2c5 0 9 3 9 7s-4 7-9 7c-1 0-2 0-3-.3L2 18l1.5-4C2 12.7 1 11 1 9c0-4 4-7 9-7z" fill="#d98a4a"/><circle cx="6" cy="9" r="1.2" fill="#fff"/><circle cx="10" cy="9" r="1.2" fill="#fff"/><circle cx="14" cy="9" r="1.2" fill="#fff"/></svg>6. Routing &amp; Messages</div>
    <div class="grid-row col-head"><div>Task</div><div class="rate"><svg viewBox="0 0 57 14"><text x="1" y="11" textLength="55" lengthAdjust="spacingAndGlyphs">Self Rating (1-5)</text></svg></div><div class="notes">Notes / Issues</div></div>
    <div class="grid-row task-row"><div>Calls routed appropriately</div><div></div><div></div></div>
    <div class="grid-row task-row"><div>Messages included all required info</div><div></div><div></div></div>
    <div class="grid-row task-row"><div>Delivered 95%+ messages in 30 min</div><div></div><div></div></div>
  </div>

  <div class="section status" style="left:633px;top:329px">
    <div class="sec-head"><svg viewBox="0 0 18 20"><rect x="2" y="1" width="14" height="18" rx="1" fill="#333"/><path d="M5 5h8M5 8h8M5 11h8" stroke="#999" stroke-width="1"/><path d="M5 17v-3M8 17v-4M11 17v-2M14 17v-5" stroke="#999" stroke-width="1.4"/></svg>Daily Status Summary (Tick One)</div>
    <div class="band"><span class="dot"></span><span class="label">Excellent</span><span>All key duties completed, proactive, calm under pressure</span></div>
    <div class="band"><span class="dot"></span><span class="label">Satisfactory</span><span>Most duties completed, minor follow-up needed</span></div>
    <div class="band"><span class="dot"></span><span class="label">Needs Support</span><span>Missed urgent duties, accuracy or stress issues</span></div>
  </div>

  <div class="section reflect" style="left:633px;top:417px">
    <div class="sec-head"><svg viewBox="0 0 18 20"><rect x="2" y="2" width="13" height="17" rx="1" fill="none" stroke="#3f8d5e" stroke-width="1.4" transform="rotate(-8 9 10)"/><path d="M5 7h7M5 10h7M5 13h5" stroke="#3f8d5e" stroke-width="1.1"/></svg>Daily Reflection</div>
    <div class="band">What went well today ?<span class="fill-line"></span></div>
    <div class="band">Any issues or barriers to note ?<span class="fill-line"></span></div>
    <div class="band">Support needed from supervisor ?<span class="fill-line"></span></div>
  </div>

  <div class="section flags" style="left:633px;top:502px">
    <div class="sec-head"><span>&#9733; Stars &amp; Flags</span><svg viewBox="0 0 18 14" style="width:14px;height:12px;margin:0 -6px 0 -8px"><path d="M2 1v13" stroke="#fff" stroke-width="1.5"/><path d="M3 1h11l-3 3.5 3 3.5H3z" fill="none" stroke="#fff" stroke-width="1.3"/></svg><span>(Supervisor Use Only)</span></div>
    <div class="band"><svg viewBox="0 0 10 10"><path d="M5 0l1.5 3.3L10 3.8 7.5 6.2 8.1 10 5 8.2 1.9 10l.6-3.8L0 3.8l3.5-.5z" fill="#5a3a2a"/></svg>Excellence or above-and-beyond moments<span class="fill-line"></span></div>
    <div class="band"><svg viewBox="0 0 10 10"><path d="M1 0v10" stroke="#5a3a2a" stroke-width="1.3"/><path d="M2 0.5h7l-2 2.5 2 2.5H2z" fill="#5a3a2a"/></svg>Concerns needing follow-up/coaching<span class="fill-line" style="margin-left:6px"></span></div>
  </div>

  <div class="section manager" style="left:633px;top:572px">
    <div class="sec-head"><svg viewBox="0 0 20 20" style="width:20px"><path d="M4 3l.6 1.3 1.4.2-1 1 .2 1.4L4 6.2 2.8 6.9 3 5.5 2 4.5l1.4-.2zM10 1l.6 1.3 1.4.2-1 1 .2 1.4L10 4.2 8.8 4.9 9 3.5 8 2.5l1.4-.2zM16 3l.6 1.3 1.4.2-1 1 .2 1.4L16 6.2l-1.2.7.2-1.4-1-1 1.4-.2z" fill="#5a3fb0"/><path d="M3 11h3v8H3zM7 11l3-4c1 0 2 1 1.5 2.5L11 11h5c1 0 1.8 1 1.5 2l-1.5 5c-.3.7-1 1-1.7 1H7z" fill="#5a3fb0"/></svg>Manager's Overall Rating</div>
    <div class="band">Please rate overall performance on a 1-5 scale</div>
    <div class="band">Manager Overall Rating<span class="fill-line short"></span></div>
  </div>

  <div class="abs sign-box">
    <div class="sign-line">Receptionist Sign.<span class="fill-line"></span></div>
    <div class="sign-line">Supervisor Sign.<span class="fill-line"></span></div>
    <div class="sign-line date">Date<span class="fill-line"></span></div>
  </div>
</div>
</body>
</html>
```